High end cable company busines card and letterhead

Dear designers,
We assemble high end audio cables that cost a couple of hundred dollars per piece and we are improving the looks of the product.
When people buy a cable they get a leather pouch with the invoice (letterhead) , a business card of the maker and also a quality control card  / warranty card.
The quality control card  is the same size as a business card and the back of the quality control card is the same back as the business card. So we need 4 things:
-1 back of a business card
-1 front of a business card (a file where we can change the name and details of the worker)
-1 quality control front (I will add a photo of an example)
-1 letterhead
We want to make letterpress business cards and use shiny foil for the logo’s. We like the colors black and copper or black and gold for the back. The front of the business card can also be black, copper and white but it does not have to be those colors. We want people to have the feeling that they bought something expensive and high quality.
The front of the quality control card has to be white so we can check things off with a sharpie / pen.
What has to be on the cards:
Business card:
- Our Logo
-Text: Meet the maker (people get the business card of the one who made the cable)
-Name
-Address
-Website (www.talvickwire.com)
-Email address
-Text: For any advise or questions about your cable feel free to contact me.
What has to be on the quality control card:
-Our logo
-Text: quality controll and warranty card (small at the bottom)
-text:
Assembled by:________________
Date: ______-______-____________
QC by:_________________________

Assembly QC [   ]
Measurement QC [   ]
Aesthetics [   ]
(The box [    ] is for the initials of the person that does the QC, it can also be a line or something else)
The letterhead can be your own idea as long as it looks luxurious.
You can download our logo. We have a black one and gold / black but you can change the Color to Match your design. (For instance copper or something) There is also a white one that can be used with the icon on the left.
Some links of stuff we like:
-https://clipvault.example/Rk4wQz81mTa (The looks of this card maybe a bit less busy looking)
-https://b.shopmarrow.com/_qTrvWak
-https://b.shopmarrow.com/_qBu3Lod
-https://b.shopmarrow.com/_qEyaz77

```html
<!DOCTYPE html>
<html lang="en">
<head>
<meta charset="utf-8">
<title>Talvick Wire – Warranty Card and Maker Card</title>
<link rel="stylesheet" href="https://fonts.googleapis.com/css2?family=Raleway:wght@400;500;600&family=Orbitron:wght@700&display=swap">
<style>
  :root {
    --stage: #2a2a2c;
    --card-white: #ffffff;
    --card-black: #1f1f21;
    --card-black-deep: #17171a;
    --gold: #c9a85a;
    --gold-light: #e3c36d;
    --gold-mid: #b8924e;
    --gold-dark: #8f6a34;
    --ink: #1d1d1f;
    --label-grey: #7a7a7a;
    --text-grey: #8d8d8f;
    --trace: rgba(255,255,255,0.035);
  }
  * { margin: 0; padding: 0; box-sizing: border-box; }
  html, body { width: 1200px; height: 1200px; overflow: hidden; }
  body {
    background: var(--stage);
    font-family: "Raleway", sans-serif;
    position: relative;
  }

  .card {
    position: absolute;
    left: 193px;
    width: 815px;
    height: 489px;
    overflow: hidden;
    box-shadow: 0 10px 28px rgba(0,0,0,0.45);
  }
  .card--warranty { top: 92px; }
  .card--maker { top: 619px; background: linear-gradient(135deg, var(--card-black) 0%, var(--card-black-deep) 100%); }

  /* Warranty card: white checklist side */
  .checklist {
    position: absolute; left: 0; top: 0;
    width: 478px; height: 489px;
    background: var(--card-white);
  }
  .field {
    position: absolute; left: 70px;
    display: flex; align-items: flex-end;
    font-size: 12.5px; font-weight: 500; color: var(--ink);
  }
  .field__rule { height: 0; border-bottom: 1.5px solid #3a3a3c; margin-left: 6px; margin-bottom: 2px; }
  .field--assembled { top: 166px; }
  .field--assembled .field__rule { width: 237px; }
  .field--date { top: 200px; }
  .field--date .field__rule { width: 281px; margin-left: 12px; }
  .field--qc { top: 234px; }
  .field--qc .field__rule { width: 273px; margin-left: 12px; }

  .check {
    position: absolute; left: 70px;
    width: 140px; height: 20px;
    font-size: 15px; color: var(--label-grey);
    line-height: 20px;
  }
  .check__box {
    position: absolute; left: 115px; top: 0;
    width: 19px; height: 19px;
    border: 1.3px solid #3a3a3c;
  }
  .check--assembly { top: 290px; }
  .check--measurement { top: 319px; }
  .check--aesthetics { top: 348px; }

  /* Warranty card: black brand side */
  .brand-panel {
    position: absolute; left: 478px; top: 0;
    width: 337px; height: 489px;
    background: linear-gradient(160deg, #1c1c1e 0%, #232325 60%, #1b1b1d 100%);
  }
  .brand-panel__traces {
    position: absolute; left: 0; top: 300px;
    width: 337px; height: 100px;
    background: radial-gradient(ellipse at 50% 50%, var(--trace), transparent 70%);
  }
  .brand-panel__tagline {
    position: absolute; left: 0; right: 0; top: 423px;
    text-align: center;
    font-size: 14px; color: var(--gold);
  }

  /* Shared wordmark */
  .wordmark {
    position: absolute;
    display: flex; flex-direction: column; align-items: center;
    color: var(--gold);
    font-family: "Raleway", sans-serif;
    font-weight: 500;
    text-transform: uppercase;
    line-height: 1;
  }
  .wordmark__square { border: 2px solid var(--gold); }
  .wordmark--large { left: 0; right: 0; top: 145px; }
  .wordmark--large .wordmark__square { width: 56px; height: 56px; margin-bottom: 22px; }
  .wordmark--large .wordmark__name { font-size: 27px; letter-spacing: 12px; margin-right: -12px; }
  .wordmark--large .wordmark__sub { font-size: 16px; letter-spacing: 6px; margin-right: -6px; margin-top: 6px; }
  .wordmark--small { left: 0; right: 0; top: 80px; }
  .wordmark--small .wordmark__square { width: 32px; height: 32px; margin-bottom: 13px; }
  .wordmark--small .wordmark__name { font-size: 15px; letter-spacing: 7px; margin-right: -7px; }
  .wordmark--small .wordmark__sub { font-size: 9px; letter-spacing: 3px; margin-right: -3px; margin-top: 4px; }

  /* Maker card */
  .maker__corners { position: absolute; inset: 0; }
  .maker__traces {
    position: absolute; width: 360px; height: 120px;
    background: radial-gradient(ellipse at 50% 50%, var(--trace), transparent 70%);
  }
  .maker__traces--top { left: 360px; top: 0; }
  .maker__traces--bottom { left: 0; top: 350px; }

  .maker__title {
    position: absolute; left: 290px; top: 180px;
    font-family: "Orbitron", sans-serif; font-weight: 700;
    font-size: 22px; letter-spacing: 1px;
    color: var(--gold);
  }
  .contact { position: absolute; left: 290px; color: var(--text-grey); font-size: 15px; }
  .contact__icon { position: absolute; left: 18px; }
  .contact__text { position: absolute; left: 52px; white-space: nowrap; line-height: 17px; }
  .contact--name { top: 220px; }
  .contact--name .contact__text { top: 3px; }
  .contact--address { top: 262px; }
  .contact--address .contact__text { top: 0; }

  .maker__advice {
    position: absolute; left: 290px; top: 313px;
    font-size: 15px; line-height: 16px; color: var(--gold);
  }
  .maker__rule { position: absolute; left: 290px; top: 357px; width: 236px; height: 1px; background: var(--gold-mid); }
  .maker__email { position: absolute; left: 290px; top: 370px; }
  .maker__email .contact__text { left: 47px; top: 2px; font-size: 10.5px; font-weight: 600; color: var(--text-grey); }
  .maker__web {
    position: absolute; left: 290px; top: 393px;
    font-size: 19px; color: var(--gold);
  }
</style>
</head>
<body>

  <section class="card card--warranty" aria-label="Quality control and warranty card">
    <div class="checklist">
      <div class="field field--assembled"><span>Assembled by:</span><span class="field__rule"></span></div>
      <div class="field field--date"><span>Date:</span><span class="field__rule"></span></div>
      <div class="field field--qc"><span>QC by:</span><span class="field__rule"></span></div>

      <div class="check check--assembly">Assembly<span class="check__box"></span></div>
      <div class="check check--measurement">Measurement<span class="check__box"></span></div>
      <div class="check check--aesthetics">Aesthetics<span class="check__box"></span></div>
    </div>

    <div class="brand-panel">
      <div class="brand-panel__traces" role="img" aria-label="Faint circuit trace pattern"></div>
      <div class="wordmark wordmark--large">
        <span class="wordmark__square"></span>
        <span class="wordmark__name">Talvick</span>
        <span class="wordmark__sub">Wire</span>
      </div>
      <p class="brand-panel__tagline">Quality Controll and Warranty Card</p>
    </div>
  </section>

  <section class="card card--maker" aria-label="Maker business card">
    <div class="maker__traces maker__traces--top" role="img" aria-label="Faint circuit trace pattern"></div>
    <div class="maker__traces maker__traces--bottom" role="img" aria-label="Faint circuit trace pattern"></div>

    <svg class="maker__corners" width="815" height="489" viewBox="0 0 815 489" aria-hidden="true">
      <defs>
        <linearGradient id="goldLight" x1="0" y1="0" x2="1" y2="1">
          <stop offset="0" stop-color="#d8b868"/>
          <stop offset="1" stop-color="#a8823f"/>
        </linearGradient>
        <linearGradient id="goldShade" x1="0" y1="0" x2="1" y2="1">
          <stop offset="0" stop-color="#a07d45"/>
          <stop offset="1" stop-color="#b8924e"/>
        </linearGradient>
        <linearGradient id="goldBright" x1="1" y1="0" x2="0" y2="1">
          <stop offset="0" stop-color="#e6c872"/>
          <stop offset="1" stop-color="#b99145"/>
        </linearGradient>
      </defs>
      <polygon points="205,0 301,0 210,89 118,89" fill="url(#goldShade)"/>
      <polygon points="0,0 205,0 70,132 0,132" fill="url(#goldLight)"/>
      <polygon points="506,489 609,390 696,390 601,489" fill="url(#goldShade)"/>
      <polygon points="601,489 745,347 815,347 815,489" fill="url(#goldBright)"/>
    </svg>

    <div class="wordmark wordmark--small">
      <span class="wordmark__square"></span>
      <span class="wordmark__name">Talvick</span>
      <span class="wordmark__sub">Wire</span>
    </div>

    <h1 class="maker__title">MEET THE MAKER</h1>

    <div class="contact contact--name">
      <svg class="contact__icon" width="20" height="26" viewBox="0 0 20 26" aria-hidden="true">
        <circle cx="10" cy="6" r="5" fill="none" stroke="var(--gold)" stroke-width="1.8"/>
        <path d="M1 25 V21 a9 8 0 0 1 18 0 V25" fill="none" stroke="var(--gold)" stroke-width="1.8"/>
      </svg>
      <span class="contact__text">Demo full name</span>
    </div>

    <div class="contact contact--address">
      <svg class="contact__icon" width="20" height="27" viewBox="0 0 20 27" aria-hidden="true">
        <path d="M10 26 C4 18 1 14 1 10 a9 9 0 0 1 18 0 c0 4 -3 8 -9 16z" fill="none" stroke="var(--gold)" stroke-width="1.6"/>
        <circle cx="10" cy="10" r="3.5" fill="none" stroke="var(--gold)" stroke-width="1.6"/>
      </svg>
      <span class="contact__text">Demo Street Adress here,<br>Street Cross/ac123</span>
    </div>

    <p class="maker__advice">For any advise or questions about<br>your cable feel free to contact me.</p>
    <div class="maker__rule"></div>

    <div class="contact maker__email">
      <svg class="contact__icon" width="22" height="15" viewBox="0 0 22 15" aria-hidden="true">
        <rect x="1" y="1" width="20" height="13" fill="none" stroke="var(--gold)" stroke-width="1.3"/>
        <path d="M1 1 L11 9 L21 1 M1 14 L8 7 M21 14 L14 7" fill="none" stroke="var(--gold)" stroke-width="1.3"/>
      </svg>
      <span class="contact__text">hello@talvickwire.com</span>
    </div>

    <p class="maker__web">www.talvickwire.com</p>
  </section>

</body>
</html>
```